I need the following on my business card:
- Name: Dana Kellick
- License # 7M31926
- Title: Producer
- Phone: (555) 317-0964
- Email: Dana@BrightpineInsuranceServices.example

- Company: Brightpine Insurance Services
- Address: 48720 Maplecrest Ave Suite 410, Alderbrook Springs, ZZ 00421
- Website: www.BrightpineInsuranceServices.example

Also add our slogan on the card: "Steady Cover, Honest Advice"

```html
<!DOCTYPE html>
<html lang="en">
<head>
<meta charset="utf-8">
<title>Brightpine Insurance Services – Business Card</title>
<link rel="stylesheet" href="https://fonts.googleapis.com/css2?family=Montserrat:wght@400;500;700&display=swap">
<style>
  :root {
    --navy: #2e3078;
    --navy-deep: #2a2c7a;
    --navy-emboss: #24266a;
    --green: #139447;
    --ink: #1c1c1c;
    --paper: #ffffff;
    --backdrop: #e9e7e3;
  }
  * { margin: 0; padding: 0; box-sizing: border-box; }
  html, body {
    width: 916px; height: 1200px; overflow: hidden;
    background: var(--backdrop);
    font-family: "Montserrat", Arial, sans-serif;
  }
  .canvas { position: relative; width: 916px; height: 1200px; }

  .card {
    position: absolute; left: 72px; width: 774px; height: 460px;
    border-radius: 24px;
  }
  .card--front { top: 108px; background: var(--paper); }
  .card--back { top: 640px; height: 463px; background: var(--navy-deep); }

  .brand {
    position: absolute; left: 40px; top: 74px;
    display: flex; align-items: center; gap: 14px;
  }
  .brand__square { width: 22px; height: 22px; background: var(--green); }
  .brand__name {
    color: var(--navy); font-weight: 700; font-size: 31px;
    line-height: 1.15; text-transform: uppercase; letter-spacing: 0.5px;
  }

  .person { position: absolute; left: 37px; top: 190px; }
  .person__name { color: var(--navy); font-weight: 700; font-size: 28px; line-height: 1.1; }
  .person__title { color: var(--green); font-size: 16px; margin-top: 6px; }

  .details { position: absolute; left: 32px; top: 258px; color: var(--ink); font-size: 16.5px; }
  .details__address { line-height: 21px; }
  .details__license { margin-top: 12px; margin-left: 3px; }
  .contact { list-style: none; margin-top: 9px; }
  .contact li { display: flex; align-items: center; gap: 10px; height: 27px; }
  .contact svg { width: 17px; height: 17px; fill: var(--navy); flex: none; }

  .back-brand {
    position: absolute; left: 0; right: 0; top: 200px; text-align: center;
    color: var(--navy-emboss); font-weight: 700; font-size: 42px;
    line-height: 1.15; text-transform: uppercase; letter-spacing: 1px;
  }
  .slogan {
    position: absolute; left: 0; right: 0; top: 387px; text-align: center;
    color: #fff; font-weight: 700; font-size: 19px;
  }
</style>
</head>
<body>
<main class="canvas">
  <section class="card card--front">
    <div class="brand">
      <span class="brand__square"></span>
      <span class="brand__name">Brightpine<br>Insurance Services</span>
    </div>

    <div class="person">
      <h1 class="person__name">Dana Kellick</h1>
      <p class="person__title">Producer</p>
    </div>

    <div class="details">
      <p class="details__address">48720 Maplecrest Ave Suite 410,<br>Alderbrook Springs, ZZ 00421</p>
      <p class="details__license">License # 7M31926</p>
      <ul class="contact">
        <li>
          <svg viewBox="0 0 24 24" aria-hidden="true"><path d="M6.6 10.8a15.1 15.1 0 0 0 6.6 6.6l2.2-2.2a1 1 0 0 1 1-.25 11.4 11.4 0 0 0 3.6.57 1 1 0 0 1 1 1V20a1 1 0 0 1-1 1A17 17 0 0 1 3 4a1 1 0 0 1 1-1h3.5a1 1 0 0 1 1 1c0 1.25.2 2.45.57 3.57a1 1 0 0 1-.25 1z"/></svg>
          (555) 317-0964
        </li>
        <li>
          <svg viewBox="0 0 24 24" aria-hidden="true"><path d="M2 5h20v2l-10 6L2 7z M2 9l10 6 10-6v10H2z"/></svg>
          Dana@BrightpineInsuranceServices.example
        </li>
        <li>
          <svg viewBox="0 0 24 24" aria-hidden="true"><path d="M12 2a10 10 0 1 0 0 20 10 10 0 0 0 0-20zm-1 17.9A8 8 0 0 1 4.1 11H7l2 2v2l2 2zm6.9-2.6A2 2 0 0 0 16 16h-1v-3l-2-1H9V9h2l2-2V5.5a8 8 0 0 1 4.9 11.8z"/></svg>
          www.BrightpineInsuranceServices.example
        </li>
      </ul>
    </div>
  </section>

  <section class="card card--back">
    <p class="back-brand">Brightpine<br>Insurance Services</p>
    <p class="slogan">Steady Cover, Honest Advice</p>
  </section>
</main>
</body>
</html>
```